Re-Design WP Site BrightPebbles.info

Site Re-design. Also Need a Button for contact on main page. Need Great Looking products re designed. Also bonus if you can install a site SEO checker on the site.

BrightPebbles.info

```html
<!DOCTYPE html>
<html lang="en">
<head>
<meta charset="utf-8">
<title>BrightPebbles.info – FAQ</title>
<link href="https://fonts.googleapis.com/css2?family=Montserrat:wght@300;400;500;600;700;800;900&display=swap" rel="stylesheet">
<style>
  :root {
    --navy: #0f1756;
    --blue: #0096e6;
    --pale-blue: #e4f2fc;
    --panel: #f3f4f8;
    --body-grey: #7a7d8c;
    --link-grey: #8a8d9a;
    --green: #1fcf6b;
    --white: #ffffff;
  }
  * { margin: 0; padding: 0; box-sizing: border-box; }
  html, body { width: 690px; height: 1200px; overflow: hidden; background: var(--white); }
  body { position: relative; font-family: "Montserrat", sans-serif; color: var(--navy); }
  .abs { position: absolute; }

  .site-header { left: 0; top: 0; width: 690px; height: 42px; background: var(--white); }
  .brand { display: flex; align-items: center; gap: 4px; font-weight: 500; color: var(--navy); white-space: nowrap; }
  .brand-dot { border-radius: 50%; background: #a9dcf7; }
  .header-brand { left: 57px; top: 16px; font-size: 11px; }
  .header-brand .brand-dot { width: 9px; height: 9px; }
  .main-nav { top: 18px; font-size: 7.5px; font-weight: 500; letter-spacing: 0.3px; color: var(--navy); display: flex; align-items: center; gap: 2px; }
  .main-nav svg { width: 5px; height: 5px; }
  .login-icon { left: 619px; top: 16px; width: 13px; height: 13px; }

  .hero { left: 0; top: 42px; width: 690px; height: 180px; background: var(--navy); }
  .hero-title { left: 0; top: 99px; width: 690px; text-align: center; color: var(--white); font-size: 27px; font-weight: 900; letter-spacing: 0.2px; }
  .pill-button { background: var(--blue); color: var(--white); border-radius: 13px; font-size: 7.2px; font-weight: 600; letter-spacing: 0.3px; display: flex; align-items: center; justify-content: center; }
  .hero-contact { left: 292px; top: 144px; width: 106px; height: 25px; }

  .faq-eyebrow { left: 0; top: 274px; width: 690px; text-align: center; color: var(--blue); font-size: 8px; font-weight: 500; }
  .faq-title { left: 0; top: 289px; width: 696px; text-align: center; font-size: 12.5px; font-weight: 800; }

  .faq-item { left: 159px; width: 372px; height: 44px; background: var(--panel); border-radius: 5px; }
  .faq-item.is-open { background: var(--pale-blue); }
  .faq-item-label { position: absolute; left: 25px; top: 16px; font-size: 8.4px; font-weight: 500; letter-spacing: 0.1px; }
  .faq-toggle { position: absolute; left: 341px; top: 13px; width: 17px; height: 17px; border-radius: 50%; background: var(--white); display: flex; align-items: center; justify-content: center; }
  .is-open .faq-toggle { background: var(--blue); }
  .faq-toggle svg { width: 7px; height: 7px; }

  .faq-body { left: 182px; top: 466px; width: 338px; font-size: 6.7px; line-height: 11.8px; color: var(--body-grey); font-weight: 400; }
  .check-list { left: 186px; top: 551px; list-style: none; font-size: 7px; color: var(--navy); font-weight: 400; }
  .check-list li { height: 14.8px; display: flex; align-items: center; gap: 8px; }
  .check-list svg { width: 10px; height: 8px; }
  .smm-button { left: 183px; top: 650px; width: 124px; height: 25px; gap: 22px; }
  .smm-button svg { width: 7px; height: 7px; }

  .site-footer { left: 0; top: 1017px; width: 690px; height: 151px; background: var(--panel); }
  .footer-brand { left: 56px; top: 1082px; font-size: 11px; }
  .footer-brand .brand-dot { width: 9px; height: 9px; }
  .footer-col { top: 1049px; font-size: 5.5px; color: var(--link-grey); }
  .footer-col h4 { font-size: 5.5px; font-weight: 500; color: #2b2f4a; margin-bottom: 18px; }
  .footer-col ul { list-style: none; }
  .footer-col li { height: 11.8px; font-weight: 400; letter-spacing: 0.2px; }
  .copyright { left: 0; top: 1183px; width: 690px; text-align: center; font-size: 4.6px; color: #9a9cab; }
  .copyright b { font-weight: 800; }
</style>
</head>
<body>

<header class="site-header abs"></header>
<div class="brand header-brand abs"><span>BrightPebbles.info</span><span class="brand-dot"></span></div>

<nav>
  <span class="main-nav abs" style="left:329px">Home</span>
  <span class="main-nav abs" style="left:382px">Services <svg viewBox="0 0 10 10"><path d="M2 3.5 5 6.5 8 3.5" fill="none" stroke="#0f1756" stroke-width="1.8"/></svg></span>
  <span class="main-nav abs" style="left:450px">Packages <svg viewBox="0 0 10 10"><path d="M2 3.5 5 6.5 8 3.5" fill="none" stroke="#0f1756" stroke-width="1.8"/></svg></span>
  <span class="main-nav abs" style="left:520px">About</span>
  <span class="main-nav abs" style="left:569px">Contact</span>
  <svg class="login-icon abs" viewBox="0 0 24 24" fill="none" stroke="#0f1756" stroke-width="2.4" stroke-linecap="round" stroke-linejoin="round"><path d="M14 3h5v18h-5"/><path d="M3 12h12"/><path d="M10 7l5 5-5 5"/></svg>
</nav>

<section class="hero abs"></section>
<h1 class="hero-title abs">We Can Help!</h1>
<div class="pill-button hero-contact abs">Contact</div>

<p class="faq-eyebrow abs">FAQ</p>
<h2 class="faq-title abs">What you will receive with Every Campaign</h2>

<div class="faq-item abs" style="top:358px"><span class="faq-item-label">WEBSITE</span><span class="faq-toggle"><svg viewBox="0 0 10 10"><path d="M2 3.5 5 6.5 8 3.5" fill="none" stroke="#0f1756" stroke-width="1.8"/></svg></span></div>
<div class="faq-item is-open abs" style="top:411px"><span class="faq-item-label">SOCIAL MEDIA MARKETING</span><span class="faq-toggle"><svg viewBox="0 0 10 10"><path d="M2 6.5 5 3.5 8 6.5" fill="none" stroke="#ffffff" stroke-width="1.8"/></svg></span></div>

<p class="faq-body abs">Lorem ipsum dolor sit amet, consectetur adipiscing elit. Quisque rutrum purus in ligula tincidunt, et dapibus ligula ornare. Nullam suscipit pretium lorem nec vulputate. Morbi felis purus, dapibus sit amet lacus eu, luctus feugiat lectus. Nulla facilisi. Morbi viverra tellus ullamcorper arcu consequat, at placerat nibh tempor. Proin suscipit dictum enim. Maecenas scelerisque neque in tellus consequat semper. Pellentesque molestie sapien vitae nunc facilisis tristique. Suspendisse sagittis magna vitae sodales auctor. Cras non facilisis lectus.</p>

<ul class="check-list abs">
  <li><svg viewBox="0 0 12 10"><path d="M1 5 4.5 8.5 11 1.5" fill="none" stroke="#1fcf6b" stroke-width="2"/></svg>Donec porta sem id sodales gravida</li>
  <li><svg viewBox="0 0 12 10"><path d="M1 5 4.5 8.5 11 1.5" fill="none" stroke="#1fcf6b" stroke-width="2"/></svg>Morbi porttitor eros in neque</li>
  <li><svg viewBox="0 0 12 10"><path d="M1 5 4.5 8.5 11 1.5" fill="none" stroke="#1fcf6b" stroke-width="2"/></svg>Sed rhoncus vitae orci vel</li>
  <li><svg viewBox="0 0 12 10"><path d="M1 5 4.5 8.5 11 1.5" fill="none" stroke="#1fcf6b" stroke-width="2"/></svg>Quisque consequat pellentesque leo</li>
  <li><svg viewBox="0 0 12 10"><path d="M1 5 4.5 8.5 11 1.5" fill="none" stroke="#1fcf6b" stroke-width="2"/></svg>Suspendisse lacinia lorem lectus</li>
  <li><svg viewBox="0 0 12 10"><path d="M1 5 4.5 8.5 11 1.5" fill="none" stroke="#1fcf6b" stroke-width="2"/></svg>Curabitur eu finibus odio</li>
</ul>

<div class="pill-button smm-button abs">SMM Packages <svg viewBox="0 0 10 10" fill="none" stroke="#fff" stroke-width="1.4"><path d="M1 5h8M5.5 1.5 9 5l-3.5 3.5"/></svg></div>

<div class="faq-item abs" style="top:713px"><span class="faq-item-label">TARGETED DISPLAY</span><span class="faq-toggle"><svg viewBox="0 0 10 10"><path d="M2 3.5 5 6.5 8 3.5" fill="none" stroke="#0f1756" stroke-width="1.8"/></svg></span></div>
<div class="faq-item abs" style="top:766px"><span class="faq-item-label">EMAIL OUTREACH</span><span class="faq-toggle"><svg viewBox="0 0 10 10"><path d="M2 3.5 5 6.5 8 3.5" fill="none" stroke="#0f1756" stroke-width="1.8"/></svg></span></div>
<div class="faq-item abs" style="top:818px"><span class="faq-item-label">WEBSITE</span><span class="faq-toggle"><svg viewBox="0 0 10 10"><path d="M2 3.5 5 6.5 8 3.5" fill="none" stroke="#0f1756" stroke-width="1.8"/></svg></span></div>
<div class="faq-item abs" style="top:871px"><span class="faq-item-label">EMAIL OUTREACH</span><span class="faq-toggle"><svg viewBox="0 0 10 10"><path d="M2 3.5 5 6.5 8 3.5" fill="none" stroke="#0f1756" stroke-width="1.8"/></svg></span></div>
<div class="faq-item abs" style="top:923px"><span class="faq-item-label">WEBSITE</span><span class="faq-toggle"><svg viewBox="0 0 10 10"><path d="M2 3.5 5 6.5 8 3.5" fill="none" stroke="#0f1756" stroke-width="1.8"/></svg></span></div>

<footer class="site-footer abs"></footer>
<div class="brand footer-brand abs"><span>BrightPebbles.info</span><span class="brand-dot"></span></div>

<div class="footer-col abs" style="left:211px">
  <h4>Pages</h4>
  <ul><li>Home</li><li>Shop</li><li>Solutions</li><li>Blog</li><li>Contact</li><li>FAQ</li></ul>
</div>
<div class="footer-col abs" style="left:340px">
  <h4>Offers</h4>
  <ul><li>Page name</li><li>Page name</li><li>Page name</li><li>Page name</li><li>Page name</li><li>Page name</li></ul>
</div>
<div class="footer-col abs" style="left:463px">
  <h4>Downloads</h4>
  <ul><li>User Agreement</li><li>Privacy Policy</li><li>Refund Policy</li></ul>
</div>

<p class="copyright abs">Copyright © 2022 <b>BrightPebbles.info</b> Use of this website constitutes acceptance of our User Agreement and Privacy Policy. Image by lumenstock.com</p>

</body>
</html>
```